Thriving Mexican import business needs a new business card

Need a refresher of our current business card. Looking for a lighter background with the logo on one side. We will want this file to be adjustable so we can change names, emails and mobile numbers.
We are open to ideas but maintaining a professional image is critical.
Thankyou,

Target Market(s)

Anyone in food industry

Industry/Entity Type

Wholesale

Contact Information for Business Card

Mark Vellanoweth
Director
Corvan Products & Liquor Pty Ltd
5B Larkfield Ct, Brimsworth VIC 3051
0491325067 (03) 95147286
mark@corvanimports.com.au
corvanimportedgoodsandspirits.com.au

Font styles to use
Serif
Other font styles liked:
• NeoGram Heavy

Requirements
Must have
• Professional yet memorable
Corvan logo
Nice to have
• Chilli or tequila/mexican food pictures
Should not have
• Dark background

```html
<!DOCTYPE html>
<html lang="en">
<head>
<meta charset="utf-8">
<title>Corvan Business Card</title>
<link href="https://fonts.googleapis.com/css2?family=Oswald:wght@600;700&family=Poppins:wght@400;500&display=swap" rel="stylesheet">
<style>
  :root {
    --page-bg: #d9d7d2;
    --card-light: #ebeae1;
    --card-dark: #151515;
    --ink: #1c1c1c;
    --silver: #c9c9c9;
    --silver-muted: #9a9a9a;
  }
  * { box-sizing: border-box; margin: 0; padding: 0; }
  html, body {
    width: 1200px; height: 1008px; overflow: hidden;
    background: var(--page-bg);
  }
  .sheet {
    width: 1200px; height: 1008px;
    display: flex; flex-direction: column;
    align-items: center; justify-content: center; gap: 40px;
  }
  .card {
    width: 760px; height: 434px;
    border-radius: 4px;
    box-shadow: 0 6px 18px rgba(0,0,0,.18);
    position: relative;
  }
  .card--front { background: var(--card-light); color: var(--ink); }
  .card--back { background: var(--card-dark); color: var(--silver);
    display: flex; flex-direction: column; align-items: center; justify-content: center; gap: 18px; }

  .brand {
    display: flex; align-items: center; gap: 14px;
    font-family: "Oswald", sans-serif; font-weight: 700;
    text-transform: uppercase; letter-spacing: 2px; line-height: 1;
  }
  .brand__mark { background: currentColor; }
  .card--front .brand { position: absolute; left: 70px; top: 110px; font-size: 62px; }
  .card--front .brand__mark { width: 22px; height: 22px; }
  .card--back .brand { font-size: 84px; color: var(--silver); }
  .card--back .brand__mark { width: 28px; height: 28px; }

  .contact {
    position: absolute; left: 400px; top: 150px;
    font-family: "Poppins", sans-serif; font-size: 15px;
  }
  .contact__name {
    font-family: "Oswald", sans-serif; font-weight: 700;
    text-transform: uppercase; font-size: 21px; letter-spacing: .5px; line-height: 1.1;
  }
  .contact__role {
    font-family: "Oswald", sans-serif; font-weight: 600;
    text-transform: uppercase; font-size: 14px; letter-spacing: .5px;
  }
  .contact__rule { width: 140px; height: 1.5px; background: var(--ink); margin: 10px 0 12px; }
  .contact__list { list-style: none; display: flex; flex-direction: column; gap: 4px; }
  .contact__item { display: flex; align-items: center; gap: 10px; line-height: 1.3; }
  .contact__icon { width: 13px; height: 13px; flex: none; fill: var(--ink); }

  .website {
    font-family: "Oswald", sans-serif; font-weight: 600;
    text-transform: uppercase; font-size: 17px; letter-spacing: 1px; color: var(--silver-muted);
  }
</style>
</head>
<body>
<main class="sheet">
  <section class="card card--front" aria-label="Business card front">
    <div class="brand"><span class="brand__mark"></span><span class="brand__name">Corvan</span></div>
    <div class="contact">
      <p class="contact__name">Mark Vellanoweth</p>
      <p class="contact__role">Director</p>
      <div class="contact__rule"></div>
      <ul class="contact__list">
        <li class="contact__item">
          <svg class="contact__icon" viewBox="0 0 16 16"><path d="M8 0a5.5 5.5 0 0 0-5.5 5.5C2.5 10 8 16 8 16s5.5-6 5.5-10.5A5.5 5.5 0 0 0 8 0zm0 8a2.5 2.5 0 1 1 0-5 2.5 2.5 0 0 1 0 5z"/></svg>
          <span>5B Larkfield Ct, Brimsworth VIC 3051</span>
        </li>
        <li class="contact__item">
          <svg class="contact__icon" viewBox="0 0 16 16"><path d="M3.6 1 6 3.6 4.7 5.5c.9 2.2 2.6 3.9 4.8 4.8L11.4 9 14 11.4 12.6 15C6.5 14.6 1.4 9.5 1 3.4z"/></svg>
          <span>0491325067</span>
        </li>
        <li class="contact__item">
          <svg class="contact__icon" viewBox="0 0 16 16"><path d="M4.5 0h7A1.5 1.5 0 0 1 13 1.5v13a1.5 1.5 0 0 1-1.5 1.5h-7A1.5 1.5 0 0 1 3 14.5v-13A1.5 1.5 0 0 1 4.5 0zM5 2v10h6V2zm3 11a1 1 0 1 0 0 2 1 1 0 0 0 0-2z"/></svg>
          <span>(03) 95147286</span>
        </li>
        <li class="contact__item">
          <svg class="contact__icon" viewBox="0 0 16 16"><path d="M0 3h16v1.2L8 9 0 4.2zm0 2.6 8 4.8 8-4.8V13H0z"/></svg>
          <span>mark@corvanimports.com.au</span>
        </li>
      </ul>
    </div>
  </section>

  <section class="card card--back" aria-label="Business card back">
    <div class="brand"><span class="brand__mark"></span><span class="brand__name">Corvan</span></div>
    <p class="website">corvanimportedgoodsandspirits.com.au</p>
  </section>
</main>
</body>
</html>
```